Marisol's Henna Party Invitation on March 20, 2026

I'd like to design an invitation that would be sent via text and posted on social media for my niece's henna party. The color scheme would be white, gold, and black. I want it to be elegant and classy. The font could be something like Rastanty Cortez. The party would be on March 20, 2026. It's a traditional and cultural type of party (pre-wedding party). I've attached some ideas for inspiration and to get a feel of a henna party.

Target Market(s)

This invitation would only be sent via text to our guests and posted on social media.

Font styles to use
Decorative
Script
Other font styles liked:
• Rastanty Cortez

Requirements
Must have
• Elegance, classy, a henna party reflection but something elegant and perhaps abstract.
Nice to have
• Something reflecting the henna party tradition. It could be a high gold candle, a decorated tray, etc. But I want it to be elegant and less crowded of an invitation.

```html
<!DOCTYPE html>
<html lang="en">
<head>
<meta charset="UTF-8">
<title>Henna Night Invitation</title>
<link href="https://fonts.googleapis.com/css2?family=Cinzel:wght@400;500&family=Cormorant+Garamond:wght@400;500;600&family=Kaushan+Script&family=Great+Vibes&family=Dancing+Script:wght@500&display=swap" rel="stylesheet">
<style>
  :root {
    --cream: #faf7f0;
    --cream-deep: #f0eadc;
    --gold: #c9a227;
    --gold-soft: #dcc07a;
    --gold-pale: #eee3c4;
    --ink: #1d1a17;
    --ink-soft: #4a443d;
    --page: #e6e6e6;
  }
  * { margin: 0; padding: 0; box-sizing: border-box; }
  html, body {
    width: 853px; height: 1200px; overflow: hidden;
    background: var(--page);
  }
  .invitation {
    position: relative;
    width: 853px; height: 1200px;
    background: radial-gradient(ellipse at 50% 45%, var(--cream) 0%, var(--cream) 60%, var(--cream-deep) 100%);
    text-align: center;
    color: var(--ink);
  }
  .frame {
    position: absolute; inset: 26px;
    border: 2px solid var(--gold-soft);
  }
  .frame::after {
    content: ""; position: absolute; inset: 6px;
    border: 1px solid var(--gold-pale);
  }
  .ornament {
    position: absolute; left: 50%; transform: translateX(-50%);
    width: 240px; height: 62px;
  }
  .ornament--top {
    top: 28px; border-radius: 0 0 120px 120px;
    background: linear-gradient(180deg, var(--gold) 0%, var(--gold-soft) 100%);
  }
  .ornament--bottom {
    bottom: 28px; border-radius: 120px 120px 0 0;
    background: linear-gradient(0deg, var(--gold) 0%, var(--gold-soft) 100%);
  }
  .eyebrow {
    position: absolute; top: 150px; left: 0; right: 0;
    font-family: "Cinzel", serif; font-size: 19px; letter-spacing: 2.5px;
    color: var(--ink-soft);
  }
  .title {
    position: absolute; top: 180px; left: 0; right: 0;
    font-family: "Kaushan Script", cursive; font-size: 96px; font-weight: 400; line-height: 1.1;
    color: var(--gold);
  }
  .honor {
    position: absolute; top: 320px; left: 0; right: 0;
    font-family: "Cormorant Garamond", serif; font-size: 27px; font-weight: 500;
    color: var(--ink-soft);
  }
  .honoree {
    position: absolute; top: 352px; left: 0; right: 0;
    font-family: "Great Vibes", cursive; font-size: 112px; line-height: 1.15;
    color: var(--ink);
  }
  .candle-scene {
    position: absolute; top: 530px; left: 50%; transform: translateX(-50%);
    width: 420px; height: 270px;
    border-radius: 14px;
    background: linear-gradient(180deg, var(--cream) 0%, #f6eed6 45%, var(--gold-pale) 100%);
  }
  .date {
    position: absolute; top: 850px; left: 0; right: 0;
    font-family: "Cormorant Garamond", serif; font-size: 29px; font-weight: 600;
    color: var(--ink);
  }
  .time {
    position: absolute; top: 900px; left: 0; right: 0;
    font-family: "Cormorant Garamond", serif; font-size: 23px;
    color: var(--ink-soft);
  }
  .dress-note {
    position: absolute; top: 1000px; left: 0; right: 0;
    font-family: "Dancing Script", cursive; font-size: 40px; font-weight: 500;
    color: var(--gold);
  }
</style>
</head>
<body>
  <main class="invitation">
    <div class="frame"></div>
    <div class="ornament ornament--top" role="img" aria-label="Gold mandala ornament hanging from the top border"></div>

    <p class="eyebrow">YOU ARE WARMLY INVITED TO CELEBRATE</p>
    <h1 class="title">Henna Night</h1>
    <p class="honor">In honor of</p>
    <p class="honoree">Bride's Name</p>

    <div class="candle-scene" role="img" aria-label="Tall white candle with a glowing flame resting on a drift of gold sand"></div>

    <p class="date">Friday, March 20, 2026</p>
    <p class="time">Evening Celebration</p>
    <p class="dress-note">Traditional attire encouraged</p>

    <div class="ornament ornament--bottom" role="img" aria-label="Gold mandala ornament rising from the bottom border"></div>
  </main>
</body>
</html>
```